Powerpoint Slide Deck

I had my logo designed using drafthollow and would like to have a professional looking powerpoint deck created with my logo etc. my website is vantreo.info

```html
<!DOCTYPE html>
<html lang="en">
<head>
<meta charset="utf-8">
<title>Vantreo Slide Deck Overview</title>
<link href="https://fonts.googleapis.com/css2?family=Poppins:ital,wght@0,300;0,400;0,500;0,600;0,700;1,400&display=swap" rel="stylesheet">
<style>
:root{
  --blue:#1a7bbf;
  --purple:#9c2a86;
  --stage:#d4d5d9;
  --ink:#3c3f45;
  --muted:#8a8d93;
  --soft:#eceef1;
  --white:#ffffff;
}
*{box-sizing:border-box;margin:0;padding:0}
html,body{width:1200px;height:850px;overflow:hidden;background:var(--stage);font-family:'Poppins',sans-serif}
.deck{position:relative;width:1200px;height:850px}
.slide{position:absolute;width:176px;height:99px;background:var(--white);overflow:hidden;box-shadow:0 2px 4px rgba(0,0,0,.18)}
.slide.blue{background:var(--blue)}
.slide.purple{background:var(--purple)}
.foot{position:absolute;left:0;right:0;bottom:0;height:4px;background:var(--blue)}
.foot .brand{position:absolute;left:4px;bottom:1px;background:var(--white);font:600 2.6px 'Poppins',sans-serif;color:var(--blue);padding:0 1px;line-height:4px}
.foot .pg{position:absolute;right:8px;top:0;font:400 1.8px 'Poppins',sans-serif;color:var(--white);line-height:4px}
.ttl{position:absolute;top:8px;left:0;right:0;text-align:center;font:600 4.6px 'Poppins',sans-serif;color:var(--blue)}
.ttl::before{content:"";display:block;width:6px;height:.4px;background:var(--blue);margin:0 auto 1px}
.sub{position:absolute;top:15px;left:0;right:0;text-align:center;font:400 1.9px 'Poppins',sans-serif;color:var(--ink)}
.tx{position:absolute;font:400 1.9px/1.4 'Poppins',sans-serif;color:var(--ink)}
.hd{position:absolute;font:600 2.6px 'Poppins',sans-serif;color:var(--blue)}
.ph{position:absolute;background:linear-gradient(135deg,#8a9aa6,#c9b9a6)}
.circ{position:absolute;border-radius:50%;background:linear-gradient(135deg,#c6a88d,#6d5a4d)}
.abs{position:absolute}
.toc-row{position:absolute;width:40px;height:3px;border-bottom:.4px solid var(--blue);display:flex;justify-content:space-between;align-items:flex-end;font:400 2.2px/1 'Poppins',sans-serif;color:var(--ink)}
.toc-row b{font-weight:600}
</style>
</head>
<body>
<main class="deck">

<!-- Row 1 -->
<section class="slide" style="left:54px;top:57px">
  <div class="ph" role="img" aria-label="Photo of a person working on a laptop" style="left:0;top:0;width:176px;height:51px;background:linear-gradient(135deg,#5d6f7c,#2a3f55)"></div>
  <div class="abs" style="left:0;top:51px;width:176px;height:48px;background:var(--blue)"></div>
  <div class="abs" style="left:8px;top:12px;font:300 8px 'Poppins',sans-serif;color:rgba(255,255,255,.8)">LOGO</div>
  <div class="abs" style="left:128px;top:0;width:48px;height:27px;background:var(--white);border-bottom-left-radius:6px;display:flex;align-items:center;justify-content:center;font:600 6px 'Poppins',sans-serif;color:var(--blue)">Vantreo</div>
  <div class="abs" style="left:9px;top:57px;font:400 6px 'Poppins',sans-serif;color:var(--white)">PRESENTATION TITLE</div>
  <div class="abs" style="left:9px;top:66px;font:600 4px 'Poppins',sans-serif;color:var(--white)">SUBTITLE</div>
  <div class="abs" style="left:8px;top:92px;font:400 2px 'Poppins',sans-serif;color:var(--white)">JANUARY 2023</div>
  <div class="abs" style="right:9px;top:92px;font:400 2px 'Poppins',sans-serif;color:var(--white)">WWW.VANTREO.INFO</div>
</section>

<section class="slide" style="left:267px;top:57px">
  <div class="ttl">Contents</div>
  <div class="toc-row" style="left:26px;top:24px">Cover Slide<b>01</b></div>
  <div class="toc-row" style="left:26px;top:37px">Contents<b>03</b></div>
  <div class="toc-row" style="left:26px;top:50px">About Us<b>04</b></div>
  <div class="toc-row" style="left:26px;top:63px">Our Mission<b>05</b></div>
  <div class="toc-row" style="left:26px;top:77px">Our Vision<b>07</b></div>
  <div class="toc-row" style="left:99px;top:24px">Infographic 1<b>01</b></div>
  <div class="toc-row" style="left:99px;top:37px">Planning<b>03</b></div>
  <div class="toc-row" style="left:99px;top:50px">Company info<b>04</b></div>
  <div class="toc-row" style="left:99px;top:63px">Our Team<b>06</b></div>
  <div class="toc-row" style="left:99px;top:77px">Dashboard<b>07</b></div>
  <div class="foot"><span class="brand">Vantreo</span><span class="pg">PAGE | 02</span></div>
</section>

<section class="slide" style="left:490px;top:57px">
  <div class="ttl">Our Vision</div>
  <div class="abs" style="left:9px;top:27px;width:167px;height:32px;background:var(--blue);padding:3px 9px;font:italic 400 3px/1.55 'Poppins',sans-serif;color:var(--white)">Lorem ipsum dolor sit amet, consectetuer adipiscing elit, sed diam nonummy nibh euismod tincidunt ut laoreet dolore magna aliquam erat volutpat. Ut wisi enim ad minim veniam, quis nostrud exerci tation ullamcorper suscipit lobortis nisl ut aliquip ex ea commodo consequat. Duis</div>
  <div class="foot"><span class="brand">Vantreo</span><span class="pg">PAGE | 03</span></div>
</section>

<section class="slide" style="left:717px;top:57px">
  <div class="ttl">Our Mission</div>
  <div class="abs" style="left:12px;top:27px;width:44px;height:24px;background:var(--soft)"></div>
  <div class="abs" style="left:124px;top:52px;width:44px;height:24px;background:var(--soft);box-shadow:0 1px 2px rgba(0,0,0,.15)"></div>
  <div class="tx" style="left:12px;top:33px;width:44px;text-align:center"><b style="color:var(--blue);font-size:2.6px">Mission 1</b><br>Lorem ipsum dolor sit amet, sed diam nonummy nibh</div>
  <div class="tx" style="left:66px;top:33px;width:44px;text-align:center"><b style="color:var(--blue);font-size:2.6px">Mission 1</b><br>Lorem ipsum dolor sit amet, sed diam nonummy nibh</div>
  <div class="tx" style="left:124px;top:33px;width:44px;text-align:center"><b style="color:var(--blue);font-size:2.6px">Mission 1</b><br>Lorem ipsum dolor sit amet, sed diam nonummy nibh</div>
  <div class="tx" style="left:12px;top:58px;width:44px;text-align:center"><b style="color:var(--blue);font-size:2.6px">Mission 1</b><br>Lorem ipsum dolor sit amet, sed diam nonummy nibh</div>
  <div class="tx" style="left:66px;top:58px;width:44px;text-align:center"><b style="color:var(--blue);font-size:2.6px">Mission 1</b><br>Lorem ipsum dolor sit amet, sed diam nonummy nibh</div>
  <div class="tx" style="left:124px;top:58px;width:44px;text-align:center"><b style="color:var(--blue);font-size:2.6px">Mission 1</b><br>Lorem ipsum dolor sit amet, sed diam nonummy nibh</div>
  <div class="foot"><span class="brand">Vantreo</span><span class="pg">PAGE | 04</span></div>
</section>

<section class="slide" style="left:934px;top:57px">
  <div class="ph" role="img" aria-label="Photo of two colleagues at a laptop" style="left:0;top:0;width:66px;height:95px;background:linear-gradient(135deg,#a9b4bb,#6e7f87)"></div>
  <div class="hd" style="left:74px;top:25px;font-size:4px">Our Acheivements</div>
  <div class="tx" style="left:74px;top:32px;width:94px">Lorem ipsum dolor sit amet, consectetuer adipiscing elit, sed diam nonummy nibh euismod tincidunt ut laoreet dolore magna aliquam erat.</div>
  <div class="abs" style="left:74px;top:50px;width:26px;height:12px;background:var(--soft);font:400 2.3px/1.3 'Poppins';color:var(--ink);padding:2px">15<br>Companies</div>
  <div class="abs" style="left:101px;top:50px;width:26px;height:12px;background:var(--soft);font:400 2.3px/1.3 'Poppins';color:var(--ink);padding:2px">1,000<br>Clients</div>
  <div class="abs" style="left:128px;top:50px;width:26px;height:12px;background:var(--purple);font:400 2.3px/1.3 'Poppins';color:var(--white);padding:2px">46<br>Employees</div>
  <div class="foot"><span class="brand">Vantreo</span><span class="pg">PAGE | 05</span></div>
</section>

<!-- Row 2 -->
<section class="slide" style="left:54px;top:190px">
  <div class="ttl">Services</div>
  <div class="sub">Lorem ipsum dolor sit amet, consectetuer adipiscing elit.</div>
  <div class="ph" role="img" aria-label="Photo of food being prepared" style="left:9px;top:26px;width:44px;height:37px;background:linear-gradient(135deg,#6b6a55,#a8997a)"></div>
  <div class="ph" role="img" aria-label="Photo of a team meeting" style="left:66px;top:26px;width:44px;height:37px;background:linear-gradient(135deg,#4e5558,#9a8c80)"></div>
  <div class="ph" role="img" aria-label="Photo of business people talking" style="left:124px;top:26px;width:44px;height:37px;background:linear-gradient(135deg,#cfd6da,#8b98a2)"></div>
  <div class="tx" style="left:9px;top:67px;width:44px;text-align:center"><b style="color:var(--purple)">Service 1</b><br>Lorem ipsum dolor sit amet, sed diam nonummy</div>
  <div class="tx" style="left:66px;top:67px;width:44px;text-align:center"><b style="color:var(--purple)">Service 2</b><br>Lorem ipsum dolor sit amet, sed diam nonummy</div>
  <div class="tx" style="left:124px;top:67px;width:44px;text-align:center"><b style="color:var(--purple)">Service 3</b><br>Lorem ipsum dolor sit amet, sed diam nonummy</div>
  <div class="foot"><span class="brand">Vantreo</span><span class="pg">PAGE | 06</span></div>
</section>

<section class="slide" style="left:267px;top:190px">
  <div class="ttl">Our Company</div>
  <div class="sub">Lorem ipsum dolor sit amet, consectetuer adipiscing elit.</div>
  <div class="tx" style="left:20px;top:29px;width:136px;text-align:center">Lorem ipsum dolor sit amet, consectetuer adipiscing elit, sed diam nonummy nibh euismod tincidunt ut laoreet dolore magna aliquam erat volutpat. Ut wisi enim ad minim veniam, quis nostrud exerci tation ullamcorper suscipit lobortis nisl ut aliquip ex ea commodo consequat.</div>
  <div class="tx" style="left:8px;top:69px;width:30px;text-align:center"><b style="color:var(--blue);font-size:2.8px">2100</b><br>Evaluations</div>
  <div class="tx" style="left:42px;top:69px;width:40px;text-align:center"><b style="color:var(--blue);font-size:2.8px">3100</b><br>Production profitably</div>
  <div class="abs" style="left:101px;top:67px;width:25px;height:11px;background:var(--purple);font:400 2px/1.4 'Poppins';color:var(--white);text-align:center;padding-top:2px"><b style="font-size:2.8px">2100</b><br>Companies</div>
  <div class="tx" style="left:140px;top:69px;width:30px;text-align:center"><b style="color:var(--blue);font-size:2.8px">14</b><br>Certifications</div>
  <div class="foot"><span class="brand">Vantreo</span><span class="pg">PAGE | 07</span></div>
</section>

<section class="slide" style="left:490px;top:190px">
  <div class="ttl">Analysis Chart</div>
  <div class="hd" style="left:9px;top:28px;font-size:2.4px">Bar Chart</div>
  <svg class="abs" style="left:9px;top:38px" width="78" height="30" viewBox="0 0 78 30">
    <g fill="var(--blue)"><rect x="8" y="2" width="20" height="2"/><rect x="8" y="10" width="20" height="2"/><rect x="8" y="18" width="20" height="2"/><rect x="8" y="26" width="20" height="2"/></g>
    <g fill="var(--purple)"><rect x="28" y="2" width="12" height="2"/><rect x="28" y="10" width="8" height="2"/><rect x="28" y="18" width="10" height="2"/><rect x="28" y="26" width="6" height="2"/></g>
    <g fill="#8a8d93"><rect x="40" y="2" width="30" height="2"/><rect x="36" y="10" width="22" height="2"/><rect x="38" y="18" width="20" height="2"/><rect x="34" y="26" width="18" height="2"/></g>
  </svg>
  <div class="tx" style="left:94px;top:27px;width:72px"><b style="color:var(--blue)">Analysis 1</b><br>Lorem ipsum dolor sit amet, consectetuer adipiscing elit, sed diam nonummy.</div>
  <div class="tx" style="left:94px;top:46px;width:72px"><b style="color:var(--blue)">Analysis 2</b><br>Lorem ipsum dolor sit amet, consectetuer adipiscing elit, sed diam nonummy.</div>
  <div class="tx" style="left:94px;top:65px;width:72px"><b style="color:var(--blue)">Analysis 3</b><br>Lorem ipsum dolor sit amet, consectetuer adipiscing elit, sed diam nonummy.</div>
  <div class="foot"><span class="brand">Vantreo</span><span class="pg">PAGE | 08</span></div>
</section>

<section class="slide" style="left:717px;top:190px">
  <div class="ttl">S.W.O.T Analysis</div>
  <div class="tx" style="left:30px;top:20px;width:116px;text-align:center">Lorem ipsum dolor sit amet, consectetuer adipiscing elit, sed diam nonummy nibh euismod tincidunt ut laoreet dolore magna.</div>
  <div class="abs" style="left:45px;top:42px;width:42px;height:57px;background:var(--blue)"></div>
  <div class="abs" style="left:129px;top:42px;width:42px;height:57px;background:var(--blue)"></div>
  <div class="tx" style="left:8px;top:46px;width:34px"><b style="color:var(--blue)">Strength</b><br>1. Lorem ipsum dolor<br>2. Consectetuer elit<br>3. Sed diam nonummy</div>
  <div class="tx" style="left:48px;top:46px;width:36px;color:var(--white)"><b>Weakness</b><br>1. Lorem ipsum dolor<br>2. Consectetuer elit<br>3. Sed diam nonummy</div>
  <div class="tx" style="left:90px;top:46px;width:36px"><b style="color:var(--blue)">Opportunity</b><br>1. Lorem ipsum dolor<br>2. Consectetuer elit<br>3. Sed diam nonummy</div>
  <div class="tx" style="left:132px;top:46px;width:36px;color:var(--white)"><b>Threat</b><br>1. Lorem ipsum dolor<br>2. Consectetuer elit<br>3. Sed diam nonummy</div>
  <div class="foot"><span class="brand">Vantreo</span><span class="pg">PAGE | 09</span></div>
</section>

<section class="slide" style="left:934px;top:190px">
  <div class="ph" role="img" aria-label="Photo of a man working on a laptop" style="left:0;top:0;width:67px;height:77px;background:linear-gradient(135deg,#39506a,#8a7b68)"></div>
  <div class="hd" style="left:87px;top:24px;font-size:4px">Process</div>
  <div class="tx" style="left:87px;top:31px;width:82px">Lorem ipsum dolor sit amet, consectetuer adipiscing elit, sed diam nonummy nibh.</div>
  <svg class="abs" style="left:67px;top:38px" width="40" height="42" viewBox="0 0 40 42" fill="none" stroke="var(--blue)" stroke-width=".4">
    <path d="M0 20 L6 6 H22 M0 20 L6 18 H30 M0 20 L6 30 H34"/>
  </svg>
  <div class="tx" style="left:89px;top:42px;width:80px"><b style="color:var(--blue)">Step 1</b><br>Lorem ipsum dolor sit amet, sed diam nonummy.</div>
  <div class="tx" style="left:97px;top:54px;width:72px"><b style="color:var(--blue)">Step 2</b><br>Lorem ipsum dolor sit amet, sed diam nonummy.</div>
  <div class="tx" style="left:101px;top:66px;width:68px"><b style="color:var(--blue)">Step 3</b><br>Lorem ipsum dolor sit amet, sed diam nonummy.</div>
  <div class="foot"><span class="brand">Vantreo</span><span class="pg">PAGE | 10</span></div>
</section>

<!-- Row 3 -->
<section class="slide" style="left:54px;top:313px">
  <div class="ph" role="img" aria-label="Photo of a modern house with a pool" style="left:8px;top:22px;width:73px;height:66px;background:linear-gradient(180deg,#b9d3e6,#d9c9b8 60%,#3fa5c2)"></div>
  <div class="hd" style="left:87px;top:24px;font-size:4px">Planning</div>
  <div class="tx" style="left:87px;top:31px;width:82px">Lorem ipsum dolor sit amet, consectetuer adipiscing elit, sed diam nonummy nibh euismod.</div>
  <div class="tx" style="left:87px;top:42px;width:80px"><b style="color:var(--blue)">Lorem ipsum do</b><br>• Lorem ipsum dolor sit amet<br>• Sed diam nonummy nibh<br>• Magna aliquam erat volutpat</div>
  <div class="tx" style="left:87px;top:59px;width:80px"><b style="color:var(--blue)">Lorem ipsum do</b><br>• Lorem ipsum dolor sit amet<br>• Sed diam nonummy nibh<br>• Magna aliquam erat volutpat</div>
  <div class="foot"><span class="brand">Vantreo</span><span class="pg">PAGE | 11</span></div>
</section>

<section class="slide" style="left:267px;top:313px">
  <div class="ph" role="img" aria-label="Photo of sparks in a workshop" style="left:9px;top:16px;width:37px;height:30px;background:linear-gradient(135deg,#3c2a1d,#d8a45a)"></div>
  <div class="ph" role="img" aria-label="Photo of a woman at a desk" style="left:84px;top:16px;width:37px;height:30px;background:linear-gradient(135deg,#8d7a68,#d5c7b8)"></div>
  <div class="ph" role="img" aria-label="Photo of hands holding a small house model" style="left:47px;top:47px;width:37px;height:30px;background:linear-gradient(135deg,#3a3e55,#9aa0b2)"></div>
  <div class="tx" style="left:49px;top:17px;width:33px"><b style="color:var(--blue)">Item 2</b><br>Lorem ipsum dolor sit amet, sed diam nonummy nibh.</div>
  <div class="tx" style="left:9px;top:54px;width:36px"><b style="color:var(--blue)">Item 1</b><br>Lorem ipsum dolor sit amet, sed diam nonummy nibh.</div>
  <div class="tx" style="left:87px;top:54px;width:36px"><b style="color:var(--blue)">Item 3</b><br>Lorem ipsum dolor sit amet, sed diam nonummy nibh.</div>
  <div class="hd" style="left:127px;top:24px;font-size:4px">Images</div>
  <div class="tx" style="left:127px;top:31px;width:44px">Lorem ipsum dolor sit amet, consectetuer adipiscing elit, sed diam nonummy nibh.</div>
  <div class="foot"><span class="brand">Vantreo</span><span class="pg">PAGE | 12</span></div>
</section>

<section class="slide" style="left:490px;top:313px">
  <div class="ttl">Our Leaders</div>
  <div class="sub">Lorem ipsum dolor sit amet, consectetuer adipiscing elit.</div>
  <div class="abs" style="left:0;top:23px;width:176px;height:15px;background:var(--purple)"></div>
  <div class="circ" role="img" aria-label="Portrait photo of a team leader" style="left:15px;top:29px;width:21px;height:21px;border:1px solid #fff"></div>
  <div class="circ" role="img" aria-label="Portrait photo of a team leader" style="left:57px;top:29px;width:21px;height:21px;border:1px solid #fff"></div>
  <div class="circ" role="img" aria-label="Portrait photo of a team leader" style="left:100px;top:29px;width:21px;height:21px;border:1px solid #fff"></div>
  <div class="circ" role="img" aria-label="Portrait photo of a team leader" style="left:140px;top:29px;width:21px;height:21px;border:1px solid #fff"></div>
  <div class="tx" style="left:7px;top:53px;width:37px;text-align:center"><b style="color:var(--blue)">Alex Moran</b><br>Manager<br>Lorem ipsum dolor sit amet, sed diam nonummy.</div>
  <div class="tx" style="left:49px;top:53px;width:37px;text-align:center"><b style="color:var(--blue)">Alex Moran</b><br>Manager<br>Lorem ipsum dolor sit amet, sed diam nonummy.</div>
  <div class="tx" style="left:92px;top:53px;width:37px;text-align:center"><b style="color:var(--blue)">Alex Moran</b><br>Manager<br>Lorem ipsum dolor sit amet, sed diam nonummy.</div>
  <div class="tx" style="left:132px;top:53px;width:37px;text-align:center"><b style="color:var(--blue)">Alex Moran</b><br>Manager<br>Lorem ipsum dolor sit amet, sed diam nonummy.</div>
  <div class="foot"><span class="brand">Vantreo</span><span class="pg">PAGE | 13</span></div>
</section>

<section class="slide" style="left:717px;top:313px">
  <div class="ttl">Our Team</div>
  <div class="sub">Lorem ipsum dolor sit amet, consectetuer adipiscing elit.</div>
  <div class="abs" style="left:141px;top:20px;width:35px;height:38px;background:var(--purple);border-radius:6px 0 0 6px"></div>
  <div class="circ" role="img" aria-label="Portrait photo of a team member" style="left:20px;top:25px;width:20px;height:20px"></div>
  <div class="circ" role="img" aria-label="Portrait photo of a team member" style="left:63px;top:25px;width:20px;height:20px"></div>
  <div class="circ" role="img" aria-label="Portrait photo of a team member" style="left:107px;top:25px;width:20px;height:20px"></div>
  <div class="circ" role="img" aria-label="Portrait photo of a team member" style="left:147px;top:25px;width:20px;height:20px;border:1px solid #fff"></div>
  <div class="circ" role="img" aria-label="Portrait photo of a team member" style="left:20px;top:61px;width:20px;height:20px"></div>
  <div class="circ" role="img" aria-label="Portrait photo of a team member" style="left:63px;top:61px;width:20px;height:20px"></div>
  <div class="circ" role="img" aria-label="Portrait photo of a team member" style="left:107px;top:61px;width:20px;height:20px"></div>
  <div class="circ" role="img" aria-label="Portrait photo of a team member" style="left:147px;top:61px;width:20px;height:20px"></div>
  <div class="tx" style="left:14px;top:47px;width:32px;text-align:center"><b style="color:var(--blue)">Alex Moran</b><br>Manager</div>
  <div class="tx" style="left:57px;top:47px;width:32px;text-align:center"><b style="color:var(--blue)">Alex Moran</b><br>Manager</div>
  <div class="tx" style="left:101px;top:47px;width:32px;text-align:center"><b style="color:var(--blue)">Alex Moran</b><br>Manager</div>
  <div class="tx" style="left:141px;top:47px;width:32px;text-align:center;color:#fff"><b>Alex Moran</b><br>Manager</div>
  <div class="tx" style="left:14px;top:83px;width:32px;text-align:center"><b style="color:var(--blue)">Alex Moran</b><br>Manager</div>
  <div class="tx" style="left:57px;top:83px;width:32px;text-align:center"><b style="color:var(--blue)">Alex Moran</b><br>Manager</div>
  <div class="tx" style="left:101px;top:83px;width:32px;text-align:center"><b style="color:var(--blue)">Alex Moran</b><br>Manager</div>
  <div class="tx" style="left:141px;top:83px;width:32px;text-align:center"><b style="color:var(--blue)">Alex Moran</b><br>Manager</div>
  <div class="foot"><span class="brand">Vantreo</span><span class="pg">PAGE | 14</span></div>
</section>

<section class="slide" style="left:934px;top:313px">
  <div class="ttl">Timeline</div>
  <svg class="abs" style="left:0;top:42px" width="176" height="16" viewBox="0 0 176 16">
    <line x1="12" y1="8" x2="164" y2="8" stroke="var(--muted)" stroke-width=".4" stroke-dasharray="1 1"/>
    <g font-family="Poppins" font-size="1.6" fill="#fff" text-anchor="middle">
      <circle cx="26" cy="8" r="3.2" fill="var(--blue)"/><text x="26" y="8.6">2000</text>
      <circle cx="49" cy="8" r="3.2" fill="var(--purple)"/><text x="49" y="8.6">2011</text>
      <circle cx="71" cy="8" r="3.2" fill="var(--blue)"/><text x="71" y="8.6">2015</text>
      <circle cx="94" cy="8" r="3.2" fill="var(--purple)"/><text x="94" y="8.6">2022</text>
      <circle cx="116" cy="8" r="3.2" fill="var(--blue)"/><text x="116" y="8.6">2025</text>
      <circle cx="139" cy="8" r="3.2" fill="var(--purple)"/><text x="139" y="8.6">2027</text>
    </g>
  </svg>
  <div class="tx" style="left:33px;top:22px;width:32px;text-align:center"><b style="color:var(--purple)">Item 1</b><br>Lorem ipsum dolor sit amet, sed diam.</div>
  <div class="tx" style="left:77px;top:22px;width:32px;text-align:center"><b style="color:var(--purple)">Item 1</b><br>Lorem ipsum dolor sit amet, sed diam.</div>
  <div class="tx" style="left:122px;top:22px;width:32px;text-align:center"><b style="color:var(--purple)">Item 1</b><br>Lorem ipsum dolor sit amet, sed diam.</div>
  <div class="tx" style="left:10px;top:67px;width:32px;text-align:center"><b style="color:var(--blue)">Item 1</b><br>Lorem ipsum dolor sit amet, sed diam.</div>
  <div class="tx" style="left:55px;top:67px;width:32px;text-align:center"><b style="color:var(--blue)">Item 1</b><br>Lorem ipsum dolor sit amet, sed diam.</div>
  <div class="tx" style="left:100px;top:67px;width:32px;text-align:center"><b style="color:var(--blue)">Item 1</b><br>Lorem ipsum dolor sit amet, sed diam.</div>
  <div class="foot"><span class="brand">Vantreo</span><span class="pg">PAGE | 15</span></div>
</section>

<!-- Row 4 -->
<section class="slide" style="left:54px;top:435px">
  <div class="hd" style="left:8px;top:24px;font-size:4px">Doughnut Chart</div>
  <svg class="abs" style="left:60px;top:27px" width="50" height="50" viewBox="0 0 50 50">
    <circle cx="25" cy="25" r="20" fill="none" stroke="var(--blue)" stroke-width="5" stroke-dasharray="75 126" transform="rotate(-90 25 25)"/>
    <circle cx="25" cy="25" r="20" fill="none" stroke="var(--purple)" stroke-width="5" stroke-dasharray="0 75 32 126" transform="rotate(-90 25 25)"/>
    <circle cx="25" cy="25" r="20" fill="none" stroke="#8a8d93" stroke-width="5" stroke-dasharray="0 107 10 126" transform="rotate(-90 25 25)"/>
    <circle cx="25" cy="25" r="20" fill="none" stroke="#c7c9cd" stroke-width="5" stroke-dasharray="0 117 9 126" transform="rotate(-90 25 25)"/>
  </svg>
  <div class="tx" style="left:8px;top:67px;width:40px">Lorem ipsum dolor sit amet, consectetuer adipiscing elit, sed diam nonummy nibh.</div>
  <div class="tx" style="left:66px;top:80px;width:50px">● 1st Qtr ● 2nd Qtr ● 3rd Qtr ● 4th Qtr</div>
  <div class="hd" style="left:129px;top:68px;font-size:3px;line-height:1.4">Total<br>13559</div>
  <div class="foot"><span class="brand">Vantreo</span><span class="pg">PAGE | 16</span></div>
</section>

<section class="slide" style="left:267px;top:435px">
  <div class="ttl">infographic 01</div>
  <svg class="abs" style="left:0;top:30px" width="176" height="16" viewBox="0 0 176 16">
    <line x1="20" y1="8" x2="156" y2="8" stroke="var(--muted)" stroke-width=".3"/>
    <g fill="#fff" stroke="#e0e2e5" stroke-width=".4">
      <circle cx="22" cy="8" r="7"/><circle cx="55" cy="8" r="7"/><circle cx="121" cy="8" r="7"/><circle cx="154" cy="8" r="7"/>
    </g>
    <polygon points="88,0 95,4 95,12 88,16 81,12 81,4" fill="var(--blue)"/>
    <g font-family="Poppins" font-size="1.7" text-anchor="middle" fill="var(--blue)">
      <text x="22" y="8.6">Lorem Ipsum</text><text x="55" y="8.6">Lorem Ipsum</text><text x="88" y="8.6" fill="#fff">Lorem Ipsum</text><text x="121" y="8.6">Lorem Ipsum</text><text x="154" y="8.6">Lorem Ipsum</text>
    </g>
  </svg>
  <div class="tx" style="left:10px;top:50px;width:24px;text-align:center"><b style="color:var(--blue)">Lorem Ipsum</b><br>Lorem ipsum dolor sit amet.</div>
  <div class="tx" style="left:43px;top:50px;width:24px;text-align:center"><b style="color:var(--blue)">Lorem Ipsum</b><br>Lorem ipsum dolor sit amet.</div>
  <div class="tx" style="left:76px;top:50px;width:24px;text-align:center"><b style="color:var(--blue)">Lorem Ipsum</b><br>Lorem ipsum dolor sit amet.</div>
  <div class="tx" style="left:109px;top:50px;width:24px;text-align:center"><b style="color:var(--blue)">Lorem Ipsum</b><br>Lorem ipsum dolor sit amet.</div>
  <div class="tx" style="left:142px;top:50px;width:24px;text-align:center"><b style="color:var(--blue)">Lorem Ipsum</b><br>Lorem ipsum dolor sit amet.</div>
  <div class="foot"><span class="brand">Vantreo</span><span class="pg">PAGE | 17</span></div>
</section>

<section class="slide" style="left:490px;top:435px">
  <div class="ttl">infographic 02</div>
  <div class="abs" style="left:26px;top:26px;width:12px;height:23px;border-radius:6px;background:var(--blue);font:600 2px/1.3 'Poppins';color:#fff;text-align:center;padding-top:8px">Lorem Ipsum</div>
  <div class="abs" style="left:63px;top:26px;width:12px;height:23px;border-radius:6px;background:var(--purple);font:600 2px/1.3 'Poppins';color:#fff;text-align:center;padding-top:8px">Lorem Ipsum</div>
  <div class="abs" style="left:100px;top:26px;width:12px;height:23px;border-radius:6px;background:var(--blue);font:600 2px/1.3 'Poppins';color:#fff;text-align:center;padding-top:8px">Lorem Ipsum</div>
  <div class="abs" style="left:136px;top:26px;width:12px;height:23px;border-radius:6px;background:var(--purple);font:600 2px/1.3 'Poppins';color:#fff;text-align:center;padding-top:8px">Lorem Ipsum</div>
  <div class="tx" style="left:18px;top:54px;width:28px;text-align:center">Lorem ipsum dolor sit amet, consectetuer.</div>
  <div class="tx" style="left:55px;top:54px;width:28px;text-align:center">Lorem ipsum dolor sit amet, consectetuer.</div>
  <div class="tx" style="left:92px;top:54px;width:28px;text-align:center">Lorem ipsum dolor sit amet, consectetuer.</div>
  <div class="tx" style="left:128px;top:54px;width:28px;text-align:center">Lorem ipsum dolor sit amet, consectetuer.</div>
  <svg class="abs" style="left:0;top:68px" width="176" height="10" viewBox="0 0 176 10">
    <polygon points="32,0 36.5,2.5 36.5,7.5 32,10 27.5,7.5 27.5,2.5" fill="var(--blue)"/>
    <polygon points="69,0 73.5,2.5 73.5,7.5 69,10 64.5,7.5 64.5,2.5" fill="var(--purple)"/>
    <polygon points="106,0 110.5,2.5 110.5,7.5 106,10 101.5,7.5 101.5,2.5" fill="var(--blue)"/>
    <polygon points="142,0 146.5,2.5 146.5,7.5 142,10 137.5,7.5 137.5,2.5" fill="var(--purple)"/>
  </svg>
  <div class="foot"><span class="brand">Vantreo</span><span class="pg">PAGE | 18</span></div>
</section>

<section class="slide purple" style="left:717px;top:435px">
  <div class="ttl" style="color:#fff">infographic 03</div>
  <style>.step{position:absolute;top:29px;width:31px;height:54px;background:var(--blue);border-radius:10px 10px 10px 0}.step .n{position:absolute;left:5px;top:-3px;width:21px;height:21px;border-radius:50%;background:#fff;border:1.5px solid var(--blue);color:var(--blue);font:700 5px/1 'Poppins';text-align:center;padding-top:5px}.step .n small{display:block;font:400 1.6px 'Poppins'}.step .d{position:absolute;left:3px;top:22px;width:26px;font:400 1.7px/1.4 'Poppins';color:#fff}</style>
  <div class="step" style="left:13px"><div class="n">500<small>Point A</small></div><div class="d"><b>Step One</b><br>Lorem ipsum dolor sit amet, consectetuer adipiscing elit.</div></div>
  <div class="step" style="left:55px"><div class="n">600<small>Point B</small></div><div class="d"><b>Step Two</b><br>Lorem ipsum dolor sit amet, consectetuer adipiscing elit.</div></div>
  <div class="step" style="left:97px"><div class="n">700<small>Point C</small></div><div class="d"><b>Step Three</b><br>Lorem ipsum dolor sit amet, consectetuer adipiscing elit.</div></div>
  <div class="step" style="left:138px"><div class="n">800<small>Point D</small></div><div class="d"><b>Step Four</b><br>Lorem ipsum dolor sit amet, consectetuer adipiscing elit.</div></div>
  <div class="foot"><span class="brand">Vantreo</span><span class="pg">PAGE | 19</span></div>
</section>

<section class="slide" style="left:934px;top:435px">
  <div class="ttl">Project Agenda</div>
  <div class="sub">Lorem ipsum dolor sit amet, consectetuer adipiscing elit.</div>
  <div class="abs" style="left:18px;top:27px;width:42px;height:50px;background:#fff;box-shadow:0 1px 3px rgba(0,0,0,.2)"></div>
  <div class="abs" style="left:67px;top:27px;width:42px;height:50px;background:var(--purple)"></div>
  <div class="abs" style="left:116px;top:27px;width:42px;height:50px;background:#fff;box-shadow:0 1px 3px rgba(0,0,0,.2)"></div>
  <svg class="abs" style="left:35px;top:36px" width="8" height="8" viewBox="0 0 8 8" fill="none" stroke="var(--blue)" stroke-width=".5"><circle cx="4" cy="3.5" r="2"/><path d="M3.2 6h1.6M3.4 7h1.2"/></svg>
  <svg class="abs" style="left:84px;top:36px" width="8" height="8" viewBox="0 0 8 8" fill="none" stroke="#fff" stroke-width=".5"><rect x="1" y="1.5" width="6" height="4" rx=".5"/><path d="M3 5.5 L2.5 7 L4.5 5.5"/></svg>
  <svg class="abs" style="left:133px;top:36px" width="8" height="8" viewBox="0 0 8 8" fill="var(--blue)"><circle cx="2.5" cy="3" r="1"/><circle cx="5.5" cy="3" r="1"/><path d="M1 6.5a1.5 1.5 0 0 1 3 0zM4 6.5a1.5 1.5 0 0 1 3 0z"/></svg>
  <div class="tx" style="left:21px;top:48px;width:36px;text-align:center"><b style="color:var(--blue)">23rd June</b><br>• Lorem ipsum dolor sit amet<br>• Sed diam nonummy nibh</div>
  <div class="tx" style="left:70px;top:48px;width:36px;text-align:center;color:#fff"><b>14th July</b><br>• Lorem ipsum dolor sit amet<br>• Sed diam nonummy nibh</div>
  <div class="tx" style="left:119px;top:48px;width:36px;text-align:center"><b style="color:var(--blue)">01st December</b><br>• Lorem ipsum dolor sit amet<br>• Sed diam nonummy nibh</div>
  <div class="foot"><span class="brand">Vantreo</span><span class="pg">PAGE | 20</span></div>
</section>

<!-- Row 5 -->
<section class="slide" style="left:54px;top:569px">
  <div class="ttl">Monthly Chart</div>
  <div class="sub">Lorem ipsum dolor sit amet, consectetuer adipiscing elit.</div>
  <svg class="abs" style="left:8px;top:27px" width="110" height="40" viewBox="0 0 110 40">
    <g stroke="#e3e5e8" stroke-width=".3"><line x1="6" y1="4" x2="108" y2="4"/><line x1="6" y1="12" x2="108" y2="12"/><line x1="6" y1="20" x2="108" y2="20"/><line x1="6" y1="28" x2="108" y2="28"/><line x1="6" y1="36" x2="108" y2="36"/></g>
    <polyline points="12,13 30,21 48,17 66,13 84,18 104,6" fill="none" stroke="var(--blue)" stroke-width=".7"/>
  </svg>
  <div class="tx" style="left:131px;top:28px"><b style="color:var(--blue)">May</b></div>
  <div class="abs" style="left:131px;top:32px;width:8px;height:8px;border-radius:50%;background:var(--blue);font:600 2.2px/8px 'Poppins';color:#fff;text-align:center">3.5</div>
  <div class="tx" style="left:131px;top:42px;width:38px">Lorem ipsum dolor sit amet, sed diam.</div>
  <div class="tx" style="left:131px;top:55px"><b style="color:var(--blue)">June</b></div>
  <div class="abs" style="left:131px;top:59px;width:8px;height:8px;border-radius:50%;background:var(--blue);font:600 2.2px/8px 'Poppins';color:#fff;text-align:center">5.7</div>
  <div class="tx" style="left:131px;top:69px;width:38px">Lorem ipsum dolor sit amet, sed diam.</div>
  <div class="foot"><span class="brand">Vantreo</span><span class="pg">PAGE | 21</span></div>
</section>

<section class="slide" style="left:267px;top:569px">
  <div class="ttl">Three Point Value</div>
  <div class="sub">Lorem ipsum dolor sit amet, consectetuer adipiscing elit.</div>
  <svg class="abs" style="left:8px;top:32px" width="66" height="46" viewBox="0 0 66 46">
    <polyline points="10,20 34,38 56,12" fill="none" stroke="#707377" stroke-width="4"/>
    <g fill="var(--blue)" stroke="#fff" stroke-width=".8"><circle cx="10" cy="20" r="6"/><circle cx="34" cy="38" r="6"/><circle cx="56" cy="12" r="6"/></g>
    <g font-family="Poppins" font-weight="600" font-size="3.5" fill="#fff" text-anchor="middle"><text x="10" y="21.3">1.</text><text x="34" y="39.3">2.</text><text x="56" y="13.3">3.</text></g>
  </svg>
  <div class="tx" style="left:88px;top:36px;width:80px"><b style="color:var(--purple);font-size:2.6px">56%</b><br>Lorem ipsum dolor sit amet, consectetuer adipiscing elit.</div>
  <div class="tx" style="left:88px;top:53px;width:80px"><b style="color:var(--purple);font-size:2.6px">70%</b><br>Lorem ipsum dolor sit amet, consectetuer adipiscing elit.</div>
  <div class="tx" style="left:88px;top:69px;width:80px"><b style="color:var(--purple);font-size:2.6px">81%</b><br>Lorem ipsum dolor sit amet, consectetuer adipiscing elit.</div>
  <div class="foot"><span class="brand">Vantreo</span><span class="pg">PAGE | 22</span></div>
</section>

<section class="slide blue" style="left:490px;top:569px">
  <div class="ttl" style="color:#fff">Table</div>
  <div class="sub" style="color:#fff">Lorem ipsum dolor sit amet, consectetuer adipiscing elit.</div>
  <style>.tbl{position:absolute;left:25px;top:26px;width:125px;border-collapse:collapse;font:400 1.8px/1.2 'Poppins';color:#fff}.tbl th{background:var(--purple);font-weight:600;text-align:left;height:3.6px;padding:0 1px}.tbl td{height:5.6px;padding:0 1px}.tbl tr.alt td{background:var(--purple)}</style>
  <table class="tbl">
    <tr><th>Data Name</th><th>Product</th><th>Profit</th><th>Optional</th><th>Sold</th><th>Performance</th></tr>
    <tr><td>Data 1</td><td>Product Name</td><td>$900,000.00</td><td>Yes</td><td>70</td><td>45%</td></tr>
    <tr class="alt"><td>Data 2</td><td>Product Name</td><td>$900,000.00</td><td>No</td><td>30</td><td>20%</td></tr>
    <tr><td>Data 3</td><td>Product Name</td><td>$900,000.00</td><td>No</td><td>20</td><td>15%</td></tr>
    <tr class="alt"><td>Data 4</td><td>Product Name</td><td>$900,000.00</td><td>Yes</td><td>100</td><td>60%</td></tr>
    <tr><td>Data 5</td><td>Product Name</td><td>$900,000.00</td><td>Yes</td><td>50</td><td>40%</td></tr>
  </table>
  <div class="foot"><span class="brand">Vantreo</span><span class="pg">PAGE | 23</span></div>
</section>

<section class="slide" style="left:717px;top:569px">
  <div class="ttl">Dashboard 01</div>
  <div class="tx" style="left:10px;top:28px;width:22px;text-align:center">Customers<br><b style="color:var(--blue);font-size:2.5px">2100</b></div>
  <div class="tx" style="left:50px;top:28px;width:22px;text-align:center">Profitably<br><b style="color:var(--blue);font-size:2.5px">3100</b></div>
  <div class="abs" style="left:101px;top:26px;width:26px;height:12px;background:var(--blue);font:400 1.9px/1.4 'Poppins';color:#fff;text-align:center;padding-top:2px">Projects<br><b style="font-size:2.5px">300</b></div>
  <div class="tx" style="left:142px;top:28px;width:22px;text-align:center">Returns<br><b style="color:var(--blue);font-size:2.5px">14</b></div>
  <div class="tx" style="left:8px;top:45px;width:30px;text-align:center"><b style="color:var(--blue)">6 Active Users</b><br>Last 10 Days</div>
  <div class="tx" style="left:48px;top:45px;width:30px;text-align:center"><b style="color:var(--blue)">2 Users per sale</b><br>Last 10 Days</div>
  <svg class="abs" style="left:10px;top:55px" width="50" height="26" viewBox="0 0 50 26">
    <g fill="var(--blue)"><rect x="6" y="2" width="16" height="1.5"/><rect x="6" y="8" width="14" height="1.5"/><rect x="6" y="14" width="12" height="1.5"/><rect x="6" y="20" width="10" height="1.5"/></g>
    <g fill="var(--purple)"><rect x="22" y="2" width="6" height="1.5"/><rect x="20" y="8" width="8" height="1.5"/><rect x="18" y="14" width="6" height="1.5"/><rect x="16" y="20" width="8" height="1.5"/></g>
    <g fill="#8a8d93"><rect x="28" y="2" width="10" height="1.5"/><rect x="28" y="8" width="6" height="1.5"/><rect x="24" y="14" width="8" height="1.5"/><rect x="24" y="20" width="6" height="1.5"/></g>
  </svg>
  <svg class="abs" style="left:74px;top:56px" width="22" height="22" viewBox="0 0 22 22">
    <circle cx="11" cy="11" r="8" fill="none" stroke="var(--blue)" stroke-width="3" stroke-dasharray="32 50.3" transform="rotate(-90 11 11)"/>
    <circle cx="11" cy="11" r="8" fill="none" stroke="var(--purple)" stroke-width="3" stroke-dasharray="0 32 18.3 50.3" transform="rotate(-90 11 11)"/>
  </svg>
  <div class="tx" style="left:118px;top:58px;width:50px"><b style="color:var(--blue)">Live Profit &amp; Net Sales</b><br><span style="color:var(--blue)">Net Profit<br><b>$55.432M</b><br>Sales = 400,000</span></div>
  <div class="foot"><span class="brand">Vantreo</span><span class="pg">PAGE | 24</span></div>
</section>

<section class="slide" style="left:934px;top:569px">
  <div class="ttl">Dashboard 02</div>
  <svg class="abs" style="left:8px;top:24px" width="100" height="32" viewBox="0 0 100 32">
    <text x="2" y="2" font-family="Poppins" font-size="1.6" fill="var(--ink)">Chart Title</text>
    <g fill="var(--blue)"><rect x="10" y="5" width="2.4" height="22"/><rect x="20" y="5" width="2.4" height="22"/><rect x="30" y="5" width="2.4" height="22"/><rect x="40" y="5" width="2.4" height="22"/><rect x="50" y="5" width="2.4" height="22"/><rect x="60" y="5" width="2.4" height="22"/><rect x="70" y="5" width="2.4" height="22"/><rect x="80" y="5" width="2.4" height="22"/></g>
    <line x1="6" y1="27" x2="88" y2="27" stroke="#ccc" stroke-width=".3"/>
  </svg>
  <svg class="abs" style="left:137px;top:29px" width="22" height="22" viewBox="0 0 22 22">
    <circle cx="11" cy="11" r="10" fill="var(--blue)"/>
    <path d="M11 11 L11 1 A10 10 0 0 0 2 7 Z" fill="#8a8d93"/>
    <path d="M11 11 L2 7 A10 10 0 0 0 4 18 Z" fill="var(--purple)"/>
  </svg>
  <svg class="abs" style="left:8px;top:62px" width="162" height="20" viewBox="0 0 162 20">
    <g>
      <path d="M2 18 L2 8 L12 6 L22 10 L32 4 L36 18 Z" fill="var(--purple)"/><path d="M2 18 L2 12 L12 10 L22 14 L32 8 L36 18 Z" fill="var(--blue)"/>
      <path d="M42 18 L42 8 L52 6 L62 10 L72 4 L76 18 Z" fill="var(--purple)"/><path d="M42 18 L42 12 L52 10 L62 14 L72 8 L76 18 Z" fill="var(--blue)"/>
      <path d="M84 18 L84 8 L94 6 L104 10 L114 4 L118 18 Z" fill="var(--purple)"/><path d="M84 18 L84 12 L94 10 L104 14 L114 8 L118 18 Z" fill="var(--blue)"/>
      <path d="M124 18 L124 8 L134 6 L144 10 L154 4 L158 18 Z" fill="var(--purple)"/><path d="M124 18 L124 12 L134 10 L144 14 L154 8 L158 18 Z" fill="var(--blue)"/>
    </g>
  </svg>
  <div class="foot"><span class="brand">Vantreo</span><span class="pg">PAGE | 25</span></div>
</section>

<!-- Row 6 -->
<section class="slide" style="left:54px;top:710px">
  <div class="ttl">Dashboard 03</div>
  <div class="tx" style="left:42px;top:16px">Chart Title</div>
  <svg class="abs" style="left:8px;top:19px" width="68" height="26" viewBox="0 0 68 26">
    <g stroke="#e3e5e8" stroke-width=".3"><line x1="4" y1="4" x2="66" y2="4"/><line x1="4" y1="12" x2="66" y2="12"/><line x1="4" y1="20" x2="66" y2="20"/></g>
    <polyline points="6,6 18,14 30,10 42,4 54,12 64,8" fill="none" stroke="var(--blue)" stroke-width=".5"/>
    <polyline points="6,16 18,8 30,16 42,12 54,6 64,14" fill="none" stroke="#707377" stroke-width=".5"/>
  </svg>
  <div class="tx" style="left:125px;top:22px">Chart Title</div>
  <svg class="abs" style="left:105px;top:25px" width="60" height="24" viewBox="0 0 60 24">
    <g fill="var(--blue)"><rect x="8" y="2" width="36" height="1.6"/><rect x="8" y="8" width="30" height="1.6"/><rect x="8" y="14" width="26" height="1.6"/><rect x="8" y="20" width="20" height="1.6"/></g>
  </svg>
  <div class="tx" style="left:42px;top:49px">Chart Title</div>
  <svg class="abs" style="left:8px;top:52px" width="76" height="32" viewBox="0 0 76 32">
    <line x1="4" y1="28" x2="74" y2="28" stroke="#ccc" stroke-width=".3"/>
    <g fill="var(--blue)"><rect x="8" y="10" width="2" height="18"/><rect x="24" y="6" width="2" height="22"/><rect x="40" y="12" width="2" height="16"/><rect x="56" y="4" width="2" height="24"/></g>
    <g fill="var(--purple)"><rect x="10.5" y="16" width="2" height="12"/><rect x="26.5" y="18" width="2" height="10"/><rect x="42.5" y="14" width="2" height="14"/><rect x="58.5" y="12" width="2" height="16"/></g>
    <g fill="#8a8d93"><rect x="13" y="20" width="2" height="8"/><rect x="29" y="14" width="2" height="14"/><rect x="45" y="20" width="2" height="8"/><rect x="61" y="18" width="2" height="10"/></g>
  </svg>
  <svg class="abs" style="left:104px;top:60px" width="8" height="8" viewBox="0 0 8 8"><circle cx="4" cy="4" r="3.6" fill="none" stroke="var(--blue)" stroke-width=".5"/><rect x="2.6" y="2.2" width="2.8" height="3.6" fill="none" stroke="var(--blue)" stroke-width=".4"/></svg>
  <div class="hd" style="left:114px;top:61px;font-size:4px">436.00</div>
  <div class="tx" style="left:104px;top:69px;width:40px">Lorem ipsum dolor sit amet, consectetuer adipiscing elit, sed diam.</div>
  <div class="foot"><span class="brand">Vantreo</span><span class="pg">PAGE | 26</span></div>
</section>

<section class="slide" style="left:267px;top:710px">
  <div class="ttl">Dashboard 04</div>
  <div class="tx" style="left:58px;top:17px">Chart Title</div>
  <svg class="abs" style="left:8px;top:20px" width="118" height="34" viewBox="0 0 118 34">
    <path d="M6 4 L30 4 L54 2 L78 6 L102 4 L112 2 L112 28 L6 28 Z" fill="#707377"/>
    <path d="M6 14 L30 12 L54 16 L78 20 L102 14 L112 12 L112 28 L6 28 Z" fill="var(--blue)"/>
  </svg>
  <div class="abs" style="left:130px;top:22px;width:18px;height:8px;background:var(--soft);font:400 1.7px/1.4 'Poppins';color:var(--blue);padding:1px">210<br>Sales</div>
  <div class="abs" style="left:130px;top:34px;width:18px;height:8px;background:var(--soft);font:400 1.7px/1.4 'Poppins';color:var(--blue);padding:1px">46<br>New Clients</div>
  <div class="abs" style="left:130px;top:46px;width:18px;height:8px;background:var(--blue);font:400 1.7px/1.4 'Poppins';color:#fff;padding:1px">15<br>Employees</div>
  <div class="tx" style="left:58px;top:61px">Chart Title</div>
  <svg class="abs" style="left:8px;top:64px" width="100" height="20" viewBox="0 0 100 20">
    <g fill="var(--blue)"><rect x="8" y="2" width="40" height="1.4"/><rect x="8" y="7" width="40" height="1.4"/><rect x="8" y="12" width="40" height="1.4"/><rect x="8" y="17" width="40" height="1.4"/></g>
    <g fill="var(--purple)"><rect x="48" y="2" width="20" height="1.4"/><rect x="48" y="7" width="14" height="1.4"/><rect x="48" y="12" width="24" height="1.4"/><rect x="48" y="17" width="12" height="1.4"/></g>
    <g fill="#8a8d93"><rect x="68" y="2" width="24" height="1.4"/><rect x="62" y="7" width="26" height="1.4"/><rect x="72" y="12" width="18" height="1.4"/><rect x="60" y="17" width="28" height="1.4"/></g>
  </svg>
  <div class="tx" style="left:128px;top:63px;width:42px"><b style="color:var(--blue)">Title</b><br>Lorem ipsum dolor sit amet, consectetuer adipiscing elit, sed diam nonummy nibh.</div>
  <div class="foot"><span class="brand">Vantreo</span><span class="pg">PAGE | 27</span></div>
</section>

<section class="slide blue" style="left:490px;top:710px">
  <div class="abs" style="left:0;right:0;top:27px;text-align:center;font:300 9px 'Poppins',sans-serif;color:#fff">THANK YOU</div>
  <div class="abs" style="left:84px;top:40px;width:8px;height:.4px;background:#fff"></div>
  <div class="abs" style="left:25px;top:43px;width:126px;text-align:center;font:400 2.3px/1.45 'Poppins',sans-serif;color:#fff">Lorem ipsum dolor sit amet, consectetuer adipiscing elit, sed diam nonummy nibh euismod tincidunt ut laoreet dolore magna aliquam erat volutpat. Ut wisi enim ad minim veniam, quis nostrud exerci tation ullamcorper suscipit lobortis nisl ut aliquip</div>
</section>

<section class="slide" style="left:717px;top:710px">
  <svg class="abs" style="left:0;top:0" width="176" height="95" viewBox="0 0 176 95" fill="none" stroke="var(--blue)" stroke-width=".5" stroke-linecap="round" stroke-linejoin="round">
    <g transform="translate(20,10)"><circle cx="3" cy="3" r="2"/><path d="M3 0v1M3 5v1M0 3h1M5 3h1"/></g>
    <g transform="translate(51,10)"><rect x=".5" y="0" width="5" height="6"/><path d="M1.5 2h3M1.5 3.5h3"/></g>
    <g transform="translate(84,10)"><circle cx="3" cy="3" r="3"/><path d="M0 3h6M3 0c-1.5 2-1.5 4 0 6M3 0c1.5 2 1.5 4 0 6"/></g>
    <g transform="translate(118,10)"><circle cx="2" cy="2" r="1.5"/><circle cx="4.5" cy="4" r="1.5"/></g>
    <g transform="translate(150,10)"><rect x="0" y="1.5" width="6" height="4.5" rx=".5"/><path d="M2 1.5V.5h2v1"/></g>
    <g transform="translate(20,28)"><circle cx="3" cy="3" r="3"/><path d="M3 1.5V3l1 1"/></g>
    <g transform="translate(51,28)"><circle cx="3" cy="3" r="2.5"/><path d="M1.5 3h3"/></g>
    <g transform="translate(84,28)"><rect x="0" y=".5" width="6" height="4" rx=".6"/><path d="M2 4.5l-.5 1.5 2-1.5"/></g>
    <g transform="translate(118,28)"><circle cx="3" cy="3" r="1.5"/><path d="M3 0v.8M3 5.2V6M0 3h.8M5.2 3H6"/></g>
    <g transform="translate(150,28)"><path d="M0 2h2l3-2v6L2 4H0z"/></g>
    <g transform="translate(20,44)"><circle cx="3" cy="3" r="2.6"/><circle cx="3" cy="3" r="1"/></g>
    <g transform="translate(51,44)"><circle cx="3" cy="2.5" r="1.8"/><path d="M2.2 5h1.6"/></g>
    <g transform="translate(84,44)" fill="var(--blue)"><circle cx="2" cy="2" r="1"/><circle cx="4.5" cy="2" r="1"/><path d="M0 6a2 2 0 0 1 4 0zM2.5 6a2 2 0 0 1 4 0z"/></g>
    <g transform="translate(118,44)"><circle cx="3" cy="3" r="2.6"/><path d="M2 2c0 1.5 1 2.5 2 2.5"/></g>
    <g transform="translate(150,44)"><path d="M0 4l2-2 2 2 2-2"/></g>
    <g transform="translate(20,62)"><path d="M0 6h6M1 6V4M3 6V2M5 6V0"/></g>
    <g transform="translate(51,62)"><rect x=".5" y="0" width="5" height="6"/><path d="M1.5 4l1 1 2-2"/></g>
    <g transform="translate(84,62)"><path d="M3 0L6 1v2.5C6 5 3 6 3 6S0 5 0 3.5V1z"/><path d="M1.8 3l1 1 1.5-1.8"/></g>
    <g transform="translate(118,62)" fill="var(--blue)"><circle cx="3" cy="1.5" r="1.2"/><circle cx="1" cy="3" r=".9"/><circle cx="5" cy="3" r=".9"/><path d="M1 6a2 2 0 0 1 4 0z"/></g>
    <g transform="translate(150,62)"><circle cx="3" cy="3" r="1.2"/><circle cx="3" cy="3" r="2.6" stroke-dasharray="1 .6"/></g>
    <g transform="translate(20,80)"><path d="M1 0v6M1 1h4l-1 1.5L5 4H1"/></g>
    <g transform="translate(51,80)"><path d="M3 0l3 1.5v3L3 6 0 4.5v-3z"/></g>
    <g transform="translate(84,80)"><path d="M3 6S.5 3.5.5 2.2a2.5 2.5 0 0 1 5 0C5.5 3.5 3 6 3 6z"/><circle cx="3" cy="2.2" r=".8"/></g>
    <g transform="translate(118,80)"><rect x="0" y="1" width="6" height="4"/><path d="M0 1l3 2 3-2"/></g>
    <g transform="translate(150,80)"><rect x=".5" y="2.5" width="5" height="3.5" rx=".4"/><path d="M1.5 2.5V1.5a1.5 1.5 0 0 1 3 0v1"/></g>
  </svg>
  <div class="foot"><span class="brand">Vantreo</span><span class="pg">PAGE | 29</span></div>
</section>

</main>
</body>
</html>
```